Tov Fiesta Mariners

We are party planning business. We are a team of established individuals and business in party stream businesses like DJ, Caterers, Party supplies, Kids parties, Events & Private Parties and much more. So basically me and business collaborate a team of business or individuals to do clients party in the best way possible.

Target Market(s)

majority of them 16 to 30 -60% to 70 % and 30 to 40 year olds- 30% to 40 %

Industry/Entity Type

Party Planning

Contact Information for Business Card

Tov
Owner & Manager
0471829354
tovfiestamariners@mailpost.example

Requirements
Must have
• front side : Logo and list of services we provide
DJ's, Catering,All party supplies, Tinyjubilee and more...just to show what the business is about when anyone looks at the card and at the rear side my details which are already provided.
Should not have
• Dont make it look we do kids party which is just one of the things we do but don't make my business card look like kids party specialist make it more connecting to youngsters and older crowd more

```html
<!DOCTYPE html>
<html lang="en">
<head>
<meta charset="utf-8">
<title>Tov Fiesta Mariners – Business Cards</title>
<link rel="stylesheet" href="https://fonts.googleapis.com/css2?family=Cutive+Mono&family=Libre+Baskerville:wght@400;700&display=swap">
<style>
  :root {
    --backdrop: #2b2b2b;
    --card: #ffffff;
    --ink: #1a1a1a;
    --accent-red: #d0202a;
    --mark-dot: #d0202a;
    --card-shadow: rgba(0,0,0,0.45);
  }
  * { margin: 0; padding: 0; box-sizing: border-box; }
  html, body {
    width: 1200px; height: 900px; overflow: hidden;
    background: var(--backdrop);
  }
  .stage {
    position: relative; width: 1200px; height: 900px;
  }
  .card {
    position: absolute; left: 320px;
    width: 560px; height: 320px;
    background: var(--card);
    border-radius: 18px;
    box-shadow: 0 10px 28px var(--card-shadow);
  }
  .card--details { top: 100px; }
  .card--services { top: 480px; }

  .brand {
    position: absolute; right: 40px; top: 50%;
    transform: translateY(-50%);
    width: 210px;
    display: flex; flex-direction: column; align-items: center; gap: 14px;
  }
  .brand__dot {
    width: 56px; height: 56px; border-radius: 50%;
    background: var(--mark-dot);
  }
  .brand__name {
    font-family: "Libre Baskerville", serif;
    font-weight: 700; font-size: 24px; line-height: 1.15;
    color: var(--accent-red); text-align: center;
  }

  .contact {
    position: absolute; left: 42px; top: 118px;
    font-family: "Libre Baskerville", serif; color: var(--ink);
  }
  .contact__head { display: flex; align-items: baseline; gap: 6px; margin-bottom: 16px; }
  .contact__name { font-size: 24px; color: var(--accent-red); letter-spacing: 1px; }
  .contact__role { font-size: 12px; }
  .contact__line { font-size: 13px; line-height: 1.45; }

  .services {
    position: absolute; left: 42px; bottom: 44px;
    font-family: "Cutive Mono", monospace;
    font-size: 22px; line-height: 1.25; color: var(--ink);
    letter-spacing: 2px;
  }
  .services li { list-style: none; }
</style>
</head>
<body>
<main class="stage">
  <section class="card card--details" aria-label="Card back with contact details">
    <div class="contact">
      <div class="contact__head">
        <span class="contact__name">TOV</span>
        <span class="contact__role">/ Owner &amp; Manager</span>
      </div>
      <p class="contact__line">0471829354</p>
      <p class="contact__line">tovfiestamariners@mailpost.example</p>
    </div>
    <div class="brand">
      <span class="brand__dot"></span>
      <span class="brand__name">Tov Fiesta Mariners</span>
    </div>
  </section>

  <section class="card card--services" aria-label="Card front with services">
    <ul class="services">
      <li>DJ's . Catering</li>
      <li>All Party Supplies</li>
      <li>Tinyjubilee and more...</li>
    </ul>
    <div class="brand">
      <span class="brand__dot"></span>
      <span class="brand__name">Tov Fiesta Mariners</span>
    </div>
  </section>
</main>
</body>
</html>
```